Corvane Electrical Solutions

On one side. LOGO (underneath:) Commercial Industrial Residential

- NAME & CONTACT DETAILS

Marcus T. Hollings
Project Manager

(Cell icon) (441) 582-6197
(Email icon) cvnelectricalsoultions@mailventra.com
(Facebook & Instagram icons )@cvnelectricalsolutions

Other side: LOGO - underneath ELECTRICAL CONSTRUCTION & MAINTENANCE . LED LIGHTING & AUTOMATION . LIFE SAFETY SYSTEMS (FIRE ALARM / SECURITY) . DATA & COMMUNICATION

```html
<!DOCTYPE html>
<html lang="en">
<head>
<meta charset="utf-8">
<title>Corvane Electrical Solutions – Business Card</title>
<link href="https://fonts.googleapis.com/css2?family=Montserrat:wght@600;700&family=Questrial&display=swap" rel="stylesheet">
<style>
  :root {
    --backdrop: #ebebeb;
    --card-dark: #4e4e4e;
    --card-teal: #0f576b;
    --white: #ffffff;
    --text-light: #f2f2f2;
  }
  html, body {
    margin: 0;
    padding: 0;
    width: 1200px;
    height: 1200px;
    overflow: hidden;
    background: var(--backdrop);
  }
  .canvas {
    position: relative;
    width: 1200px;
    height: 1200px;
  }
  .card {
    position: absolute;
    top: 451px;
    width: 522px;
    height: 298px;
    overflow: hidden;
  }
  .card--front { left: 74px; background: var(--card-dark); }
  .card--back  { left: 605px; background: var(--card-teal); }

  /* front */
  .brand-tab {
    position: absolute;
    left: 0;
    top: 115px;
    width: 248px;
    height: 72px;
    background: var(--white);
    border-radius: 0 36px 36px 0;
    display: flex;
    align-items: center;
    padding-left: 20px;
    box-sizing: border-box;
  }
  .brand-name {
    font-family: "Montserrat", sans-serif;
    font-weight: 600;
    letter-spacing: 2px;
    text-transform: uppercase;
    line-height: 1.2;
  }
  .brand-tab .brand-name {
    color: var(--card-teal);
    font-size: 12px;
  }
  .person {
    position: absolute;
    left: 280px;
    top: 47px;
    color: var(--white);
  }
  .person-name {
    font-family: "Montserrat", sans-serif;
    font-weight: 700;
    font-size: 19px;
    letter-spacing: 1px;
    margin: 0;
    text-transform: uppercase;
  }
  .person-role {
    font-family: "Questrial", sans-serif;
    font-size: 14px;
    margin: 2px 0 0;
    color: var(--text-light);
  }
  .contact-line {
    position: absolute;
    left: 276px;
    top: 112px;
    width: 2px;
    height: 120px;
    background: var(--white);
  }
  .contact-list {
    list-style: none;
    margin: 0;
    padding: 0;
  }
  .contact-item {
    position: absolute;
    left: 266px;
    display: flex;
    align-items: center;
    gap: 9px;
    font-family: "Questrial", sans-serif;
    font-size: 11px;
    color: var(--text-light);
  }
  .contact-icon {
    width: 22px;
    height: 22px;
    border-radius: 50%;
    background: var(--white);
    display: flex;
    align-items: center;
    justify-content: center;
  }

  /* back */
  .card--back .brand-name {
    position: absolute;
    left: 0;
    right: 0;
    top: 30px;
    text-align: center;
    color: var(--white);
    font-size: 17px;
    letter-spacing: 3px;
  }
  .services {
    list-style: none;
    margin: 0;
    padding: 0;
  }
  .service {
    position: absolute;
    left: 0;
    display: flex;
    align-items: center;
    font-family: "Questrial", sans-serif;
    font-size: 14px;
    color: var(--white);
    text-transform: uppercase;
  }
  .service svg { margin-right: 14px; }
</style>
</head>
<body>
<div class="canvas">

  <section class="card card--front">
    <div class="brand-tab">
      <div class="brand-name">Corvane<br>Electrical<br>Solutions</div>
    </div>

    <div class="person">
      <h1 class="person-name">Marcus T. Hollings</h1>
      <p class="person-role">Project Manager</p>
    </div>

    <div class="contact-line"></div>
    <ul class="contact-list">
      <li class="contact-item" style="top:110px">
        <span class="contact-icon">
          <svg width="12" height="12" viewBox="0 0 24 24"><path fill="#4e4e4e" d="M6.6 10.8a15.1 15.1 0 0 0 6.6 6.6l2.2-2.2c.3-.3.7-.4 1-.2 1.1.4 2.3.6 3.6.6.6 0 1 .4 1 1V20c0 .6-.4 1-1 1A17 17 0 0 1 3 4c0-.6.4-1 1-1h3.5c.6 0 1 .4 1 1 0 1.3.2 2.5.6 3.6.1.3 0 .7-.2 1z"/></svg>
        </span>
        (441) 582-6197
      </li>
      <li class="contact-item" style="top:146px">
        <span class="contact-icon">
          <svg width="12" height="10" viewBox="0 0 24 18"><rect x="1" y="1" width="22" height="16" fill="none" stroke="#4e4e4e" stroke-width="2"/><path d="M1 1l11 9 11-9M1 17l8-7M23 17l-8-7" fill="none" stroke="#4e4e4e" stroke-width="2"/></svg>
        </span>
        cvnelectricalsoultions@mailventra.com
      </li>
      <li class="contact-item" style="top:187px">
        <span class="contact-icon"><svg width="8" height="8"><circle cx="4" cy="4" r="4" fill="#4e4e4e"/></svg></span>
        cvnelectricalsolutions
      </li>
      <li class="contact-item" style="top:226px">
        <span class="contact-icon"><svg width="8" height="8"><circle cx="4" cy="4" r="4" fill="#4e4e4e"/></svg></span>
        cvnelectricalsolutions
      </li>
    </ul>
  </section>

  <section class="card card--back">
    <div class="brand-name">Corvane<br>Electrical Solutions</div>

    <ul class="services">
      <li class="service" style="top:136px">
        <svg width="103" height="14" viewBox="0 0 103 14"><rect x="0" y="5.5" width="88" height="3" fill="#fff"/><rect x="88" y="2" width="8" height="10" rx="3" fill="#fff"/><rect x="96" y="3.5" width="7" height="2" fill="#fff"/><rect x="96" y="8.5" width="7" height="2" fill="#fff"/></svg>
        Electrical Construction &amp; Maintenance
      </li>
      <li class="service" style="top:168px">
        <svg width="103" height="14" viewBox="0 0 103 14"><rect x="0" y="5.5" width="88" height="3" fill="#fff"/><rect x="88" y="2" width="8" height="10" rx="3" fill="#fff"/><rect x="96" y="3.5" width="7" height="2" fill="#fff"/><rect x="96" y="8.5" width="7" height="2" fill="#fff"/></svg>
        LED Lighting &amp; Automation
      </li>
      <li class="service" style="top:200px">
        <svg width="103" height="14" viewBox="0 0 103 14"><rect x="0" y="5.5" width="88" height="3" fill="#fff"/><rect x="88" y="2" width="8" height="10" rx="3" fill="#fff"/><rect x="96" y="3.5" width="7" height="2" fill="#fff"/><rect x="96" y="8.5" width="7" height="2" fill="#fff"/></svg>
        Life Safety Systems (Fire Alarm / Security)
      </li>
      <li class="service" style="top:232px">
        <svg width="103" height="14" viewBox="0 0 103 14"><rect x="0" y="5.5" width="88" height="3" fill="#fff"/><rect x="88" y="2" width="8" height="10" rx="3" fill="#fff"/><rect x="96" y="3.5" width="7" height="2" fill="#fff"/><rect x="96" y="8.5" width="7" height="2" fill="#fff"/></svg>
        Data &amp; Communication
      </li>
    </ul>
  </section>

</div>
</body>
</html>
```